Medical Internet Marketing Company Needs a Site!

We need a new, fresh website for our search engine optimization and social media marketing company. We specialize in helping medical practices, doctors, physicians, and hospitals with their online presence and web ranking. The site should lean towards being suited for these audiences.

We have several examples of website that we like as well as things that we like about them.

Here are sites that we enjoy.

www.brightwavelab.com

It's a good design for the site all around. The videos, buttons, and images are all excellent. They did a fine job.

- We really like their "contact us" side bar and want to include one like it on the secondary pages.

www.corvantis.net

- We don't like the "thickness" of the top navigation bar.
- We like the page colors, easy navigation, and big call to action phone number in the top right corner.

http://www.teluvo.com/

Out of all the examples provided, Teluvo is our favorite and closest look and style to what we are looking for.

- We really like the openness of the design, such as space between the text and background.

- We want a price page in a style very similar to their pricing page with the services listed and check-marks, etc. although we intend to have multiple service package columns much like Corvantis's SEO pricing page.

- The way the video fits into the home page header is very organized, simple, and attention grabbing. We intend to place a slider with videos here.

- We need a page design that will allow for an image slider like Teluvo's Features page.

Here's a great example of a medical internet marketing website: http://www.dermaplex.com/

Target Market(s)

Our target market is doctors, typically male and typically 40-45 years old. I

Industry/Entity Type

Marketing

Requirements
Must have
• The homepage should have a slider in the video. Interior pages should have a video in the very top similar to how they do it on www.brightwavelab.com

The top navigation tabs needed are:
- Home
- Solutions
- Resources
- About
- Why Quelvo
- Contact

The sidebar should have a GREAT call to action in it on interior pages.

There should be one interior page that is similar to this - http://www.teluvo.com/pricing/

There needs to be a page with multiple boxes that take up a row of the web page's body. This page will house all the case studies similar to brightwave lab's: http://www.brightwavelab.com/success-stories/case-studies/ The one exception is we want the case studies to be inside of "boxes" instead of between horizontal lines like brightwave lab's.
Nice to have
• Color, professional, and clean. GREAT use of calls to actions.

```html
<!DOCTYPE html>
<html lang="en">
<head>
<meta charset="utf-8">
<title>Quelvo — Internet Marketing &amp; Websites for Medical Practices</title>
<link href="https://fonts.googleapis.com/css2?family=Cabin:wght@400;500;600&family=Noto+Serif:wght@700&display=swap" rel="stylesheet">
<style>
:root{
  --blue:#2b8fc0;
  --teal:#1f6f86;
  --sky:#4aa0d0;
  --orange:#f7941d;
  --green:#8dc63f;
  --ink:#222;
  --body:#555;
  --grey:#9a9a9a;
  --rule:#dddddd;
  --news:#d6e8f3;
}
*{margin:0;padding:0;box-sizing:border-box}
html,body{width:1017px;height:1200px;overflow:hidden}
body{position:relative;font-family:"Cabin",sans-serif;color:var(--body);
  background:linear-gradient(#ffffff 0,#f1f1f1 405px,var(--sky) 405px,#3f97c8 1200px)}
.abs{position:absolute}
a{text-decoration:none;color:inherit}

.brand{left:98px;top:34px;display:flex;align-items:center;gap:12px}
.brand-square{width:40px;height:40px;background:var(--green)}
.brand-name{font-size:44px;font-weight:500;letter-spacing:6px;color:var(--grey);line-height:1}
.top-call{right:112px;top:32px;font-size:27px;color:var(--blue)}
.top-call span{color:var(--green)}

.main-nav{left:98px;top:104px;display:flex;font-size:15.5px;color:var(--ink)}
.main-nav a{margin-right:34.5px}
.main-nav a.active{color:var(--orange)}

.support-tab{left:981px;top:137px;width:36px;height:109px;background:var(--green);border-radius:5px 0 0 5px;
  color:#fff;font-size:15px;letter-spacing:1px;display:flex;align-items:center;justify-content:center}
.support-tab span{transform:rotate(-90deg);white-space:nowrap}

.page{left:97px;top:138px;width:820px;height:854px;background:#fff}

.video{left:106px;top:147px;width:463px;height:258px;background:#111}
.video-main{position:absolute;left:0;top:0;width:463px;height:169px;
  background:radial-gradient(ellipse at 55% 40%,#e0792a,#8a3a12 60%,#3a1606)}
.video-play{position:absolute;left:209px;top:62px;width:44px;height:44px;border-radius:50%;background:rgba(40,40,40,.55)}
.video-play::after{content:"";position:absolute;left:17px;top:12px;border-left:15px solid rgba(255,255,255,.7);border-top:10px solid transparent;border-bottom:10px solid transparent}
.video-thumbs{position:absolute;left:0;top:169px;display:flex;gap:1px}
.video-thumbs div{width:92px;height:63px}
.video-bar{position:absolute;left:0;top:232px;width:463px;height:26px;background:linear-gradient(#3a3a3a,#151515);
  color:#ddd;font-size:9px;display:flex;align-items:center;padding-left:15px;gap:14px}
.video-bar::before{content:"";position:absolute;left:0;top:0;width:46px;height:2px;background:#d22}
.video-bar .time b{color:#fff;font-weight:400}
.bar-pause{width:10px;height:11px;border-left:3px solid #ccc;border-right:3px solid #ccc}
.bar-icons{margin-left:auto;margin-right:12px;display:flex;gap:10px}
.bar-icons i{display:block;width:12px;height:9px;border:1.5px solid #bbb}

.hero{left:569px;top:147px;width:339px;height:258px;background:linear-gradient(160deg,#cfe6f4,#f4f9fd 60%,#e4f0f8)}
.hero-title{position:absolute;left:24px;top:20px;font-size:31px;line-height:30px;color:var(--teal);font-weight:400}
.hero-title span{color:var(--orange)}
.hero-list{position:absolute;left:28px;top:130px;list-style:none;font-size:11px;color:#222}
.hero-list li{margin-bottom:8.5px;padding-left:14px;position:relative}
.hero-list li::before{content:"";position:absolute;left:0;top:4px;width:7px;height:7px;border-radius:50%;background:#111}
.btn{position:absolute;top:215px;width:134px;height:41px;border-radius:4px;color:#fff;font-size:19px;font-weight:600;
  display:flex;align-items:center;justify-content:center;box-shadow:0 2px 3px rgba(0,0,0,.25)}
.btn-orange{left:24px;background:linear-gradient(#ffa733,#f07c0a)}
.btn-blue{left:173px;background:linear-gradient(#2aa6de,#136fa8)}

.service{top:436px;width:228px;height:153px;border-bottom:1px solid var(--rule)}
.service h2{font-size:16px;font-weight:400;color:var(--ink);letter-spacing:.2px}
.service p{position:absolute;top:32px;left:2px;width:150px;font-size:14px;line-height:20.3px}
.learn{color:var(--orange);font-size:14px}
.service .learn{position:absolute;left:3px;top:114px}
.globe{position:absolute;left:157px;top:43px;width:65px;height:65px;border-radius:50%;
  background:radial-gradient(circle at 35% 35%,#c9f2b5,#37a634 50%,#1b6b1d)}
.mark-square{position:absolute;left:165px;top:58px;width:32px;height:32px;background:var(--green)}

.seo{left:121px;top:614px;width:502px}
.seo h2{font-size:19px;font-weight:400;color:var(--blue);margin-bottom:12px}
.seo-photo{float:left;width:115px;height:85px;border:1px solid #ccc;padding:4px;margin:0 10px 4px 0}
.seo-photo div{width:100%;height:100%;background:linear-gradient(135deg,#e9eef2,#9fb0bd 60%,#3b8da0)}
.seo p{font-size:12.5px;line-height:18.6px;text-align:justify;color:#444}
.seo .learn{display:block;margin-top:10px}

.news{left:662px;top:617px;width:230px;height:215px;background:var(--news);padding:10px 12px}
.news h2{font-size:16.5px;font-weight:400;color:var(--ink);margin-bottom:6px}
.news a{display:block;font-size:13.5px;line-height:20.3px;color:var(--blue);padding:4px 0 7px;border-bottom:1px solid #c2d8e6}
.news a:last-child{border:0}

.cta{left:120px;top:864px;width:771px;height:102px;overflow:hidden;
  background:linear-gradient(100deg,#1c5a0e,#3e8a17 45%,#5fae22 70%,#2c7410)}
.cta-head{position:absolute;left:20px;top:16px;font-family:"Noto Serif",serif;font-size:25px;font-weight:700;color:#fff;letter-spacing:.5px}
.cta-call{position:absolute;left:111px;top:52px;font-size:31px;color:#fff}
.cta-phone{position:absolute;left:20px;top:52px}
.cta-lines{position:absolute;left:0;top:0}
.cta-or{position:absolute;left:464px;top:42px;color:#fff;font-size:16px;transform:rotate(-45deg)}
.cta-btn{position:absolute;left:524px;top:33px;width:218px;height:40px;border-radius:4px;
  background:linear-gradient(#ffa733,#f07c0a);color:#fff;font-size:19px;font-weight:600;
  display:flex;align-items:center;justify-content:center;box-shadow:0 2px 3px rgba(0,0,0,.3)}

.foot-col h3{font-size:17px;font-weight:400;color:#fff;margin-bottom:6px}
.foot-links{left:98px;top:1023px;width:217px}
.foot-links a{display:block;color:#fff;font-size:13.5px;line-height:18px;border-bottom:1px solid rgba(255,255,255,.55);padding-bottom:2px;margin-bottom:0.3px}
.foot-contact{left:379px;top:1023px;color:#fff;font-size:13.5px;line-height:20.3px}
.foot-social{left:634px;top:1021px;color:#fff}
.foot-social p{font-size:14.5px}
.follow{display:flex;align-items:center;gap:8px;margin-top:10px;font-size:17px}
.follow i{display:block;width:21px;height:21px;border-radius:50%;background:#fff;opacity:.9}
</style>
</head>
<body>

<header>
  <div class="abs brand"><span class="brand-square"></span><span class="brand-name">QUELVO</span></div>
  <div class="abs top-call"><span>Call</span> 0400 555 182</div>
  <nav class="abs main-nav">
    <a class="active" href="#">HOME</a><a href="#">WHY QUELVO</a><a href="#">PRICING</a><a href="#">SOLUTIONS</a><a href="#">FEATURES</a><a href="#">RESOURCES</a><a href="#">ABOUT</a><a href="#">CONTACT</a>
  </nav>
  <a class="abs support-tab" href="#"><span>SUPPORT</span></a>
</header>

<main>
  <div class="abs page"></div>

  <section class="abs video">
    <div class="video-main" role="img" aria-label="Video frame of a lecture hall audience watching a presentation"><div class="video-play"></div></div>
    <div class="video-thumbs">
      <div role="img" aria-label="Thumbnail of lecture hall" style="background:linear-gradient(#c86a2a,#5a2a10)"></div>
      <div role="img" aria-label="Thumbnail of classroom session" style="background:linear-gradient(#e8d9bf,#7a5a3a)"></div>
      <div role="img" aria-label="Thumbnail of presenter at screen" style="background:linear-gradient(#d8d2c2,#6b6a5e)"></div>
      <div role="img" aria-label="Thumbnail of dark auditorium" style="background:linear-gradient(#4a3a2a,#1a120a)"></div>
      <div role="img" aria-label="Thumbnail of speaker at podium" style="background:linear-gradient(#9bc8d8,#7a4a2a)"></div>
    </div>
    <div class="video-bar"><span class="bar-pause"></span><span>◀)</span><span class="time"><b>00:44</b> / 10:11</span>
      <span class="bar-icons"><i></i><i></i><i></i><i></i></span></div>
  </section>

  <section class="abs hero">
    <h1 class="hero-title">Internet Marketing<br>&amp; Websites for<br><span>Medical Practices</span></h1>
    <ul class="hero-list">
      <li>Nullam iaculis ante eu libero semper eu mattis ligula</li>
      <li>Phasellus vitae diam sit amet nibh ullamcorper</li>
      <li>Curabitur id turpis eros, at pulvinar enim.</li>
    </ul>
    <a class="btn btn-orange" href="#">Get Pricing</a>
    <a class="btn btn-blue" href="#">Features</a>
  </section>

  <section class="abs service" style="left:119px">
    <h2>MEDICAL WEBSITE SERVICES</h2>
    <p>Nullam iaculis ante eu libero semper eu mattis ligula hendrerit. Phasellus vitae diam sit</p>
    <div class="globe" role="img" aria-label="Green globe illustration"></div>
    <a class="learn" href="#">Learn More</a>
  </section>
  <section class="abs service" style="left:392px;width:230px">
    <h2>CASE STUDY</h2>
    <p>Sed lectus justo, lobortis non pellentesque eget, egestas sit amet arcu.</p>
    <svg style="position:absolute;left:159px;top:40px" width="64" height="64" viewBox="0 0 64 64" aria-hidden="true">
      <path d="M32 32 L32 0 A32 32 0 0 1 64 32 Z" fill="#8dc63f"/>
      <path d="M34 34 L66 34 A32 32 0 0 1 55 56 Z" fill="#ffb400" transform="translate(-2 -2)"/>
      <path d="M32 32 L53 54 A32 32 0 1 1 32 0 Z" fill="#2d6fd0"/>
    </svg>
    <a class="learn" href="#">Learn More</a>
  </section>
  <section class="abs service" style="left:660px;width:231px">
    <h2>WHY QUELVO?</h2>
    <p>Pellentesque eget, egestas sit amet arcu. Etiam diam libero, egestas et tincidunt id,</p>
    <span class="mark-square"></span>
    <a class="learn" href="#">Learn More</a>
  </section>

  <section class="abs seo">
    <h2>SEARCH ENGINE OPTIMIZATION</h2>
    <div class="seo-photo"><div role="img" aria-label="Tablet with medical chart and stethoscope"></div></div>
    <p>Lorem ipsum dolor sit amet, consectetur adipiscing elit. Nullam sollicitudin gravida mi, sed porttitor erat blandit vel. Donec mattis est eu tortor convallis venenatis. Sed lectus justo, lobortis non pellentesque eget, egestas sit amet arcu. Etiam diam libero, egestas et tincidunt id, dictum non nisl. Ut velit lacus, accumsan eu molestie Ut velit lacus, accumsan eu molestie sit amet, gravida at augue. Nullam et semper risus. Cum sociis natoque penatibus et magnis dis parturient montes, nascetur ridiculus mus. Sed id ipsum fringilla metus iaculis iaculis eget sit amet nibh. Cum sociis natoque penatibus et magnis dis parturient montes, nascetur ridiculus mus. Phasellus porta vehicula fringilla.</p>
    <a class="learn" href="#">Learn More</a>
  </section>

  <aside class="abs news">
    <h2>CLINOVA NEWS</h2>
    <a href="#">Nam fermentum, tortor id dignissim iaculis</a>
    <a href="#">Phasellus nulla justo, ultricies vel facilisis non, laoreet ut odio</a>
    <a href="#">Cras nunc tellus, viverra nec semper at, tristique vel dui.</a>
  </aside>

  <section class="abs cta">
    <svg class="cta-lines" width="771" height="102" aria-hidden="true">
      <line x1="526" y1="0" x2="488" y2="36" stroke="#fff" stroke-width="1.2"/>
      <line x1="458" y1="69" x2="425" y2="102" stroke="#fff" stroke-width="1.2"/>
    </svg>
    <div class="cta-head">SPEAK WITH AN EXPERT NOW</div>
    <svg class="cta-phone" width="70" height="40" viewBox="0 0 70 40" aria-hidden="true">
      <path d="M4 14 Q35 -4 66 14 L62 22 L50 18 L48 12 Q35 8 22 12 L20 18 L8 22 Z" fill="#cfe3f0"/>
      <rect x="16" y="18" width="40" height="20" rx="4" fill="#e8f2f8"/>
      <rect x="42" y="20" width="12" height="8" fill="#f7941d"/>
      <g fill="#7aa6c2"><rect x="20" y="22" width="4" height="3"/><rect x="27" y="22" width="4" height="3"/><rect x="34" y="22" width="4" height="3"/><rect x="20" y="28" width="4" height="3"/><rect x="27" y="28" width="4" height="3"/><rect x="34" y="28" width="4" height="3"/></g>
    </svg>
    <div class="cta-call">CALL - 0400 555 182</div>
    <div class="cta-or">Or</div>
    <a class="cta-btn" href="#">Schedule Consultation</a>
  </section>
</main>

<footer>
  <div class="abs foot-col foot-links">
    <h3>LINKS</h3>
    <a href="#">Why Quelvo</a><a href="#">pricing</a><a href="#">Solutions</a><a href="#">Features</a><a href="#">Resources</a><a href="#">Case Study</a>
  </div>
  <div class="abs foot-col foot-contact">
    <h3>CONTACT US</h3>
    QUELVO<br>The Harbourline Tower, 4th floor<br>K L Road, Perth (East),<br>Australia<br>Email: info@quelvo.com.au<br>Phone: 0400 555 182
  </div>
  <div class="abs foot-social">
    <p>Copyright © 2012 QUELVO. All right reserved.</p>
    <div class="follow">Follow us on <i></i><i></i><i></i><i></i></div>
  </div>
</footer>

</body>
</html>
```